Brochure and business Design Project

I need to designee brochures for my company and need material helps me to market my business.
I own a corporate housing company and accommodations services which is we rent out furnished apartment for short term lease 30 days or more and we provider many services for international patient who come to Houston Marlowe medical center for medical treatment , pleasure , business or visit we also provide help with limousine service airport pick ups , cleaning services , concierge service , car rental services , prepaid services , immigration stay extend service .
explain about services we provide and talk about our goal and the company, i need inviting colors we accommodating people like hotline and etc, my logo must be change to fit with new design, i do not want to copy and past what i have on my website or on what i sent i need better story and something to help me marking my hosting business

Target Market(s)

business material

Industry/Entity Type

Accommodation

Colors

Designer to choose colors to be used in the design.

Requirements
Must have
• explain about services we provide and talk about our goal and the company, i need inviting colors we accommodating people like hotline and etc, my logo must be change to fit with new design, i do not want to copy and past what i have on my website or on what i sent i need better story and something to help me marking my business . we accommodate patient from all over the planet who comes for medicl treatment at Marlowe medical center
Nice to have
• different langue's
Should not have
• any sexual , or religion signs

```html
<!DOCTYPE html>
<html lang="en">
<head>
<meta charset="utf-8">
<title>Harborline Stays – Brochure</title>
<link href="https://fonts.googleapis.com/css2?family=Open+Sans:wght@400;600;700;800&family=Oswald:wght@400;500&display=swap" rel="stylesheet">
<style>
:root{
  --pink:#d3104f;
  --pink-dark:#b00c41;
  --ink:#3a3a3a;
  --grey:#8a8a8a;
  --paper:#ffffff;
  --stage:#e9e7e4;
  --sky:#9fb4c9;
  --city:#6f7f74;
}
*{margin:0;padding:0;box-sizing:border-box}
html,body{width:814px;height:1200px;overflow:hidden}
body{background:var(--stage);font-family:"Open Sans",Arial,sans-serif;color:var(--ink);position:relative}
.sheet{position:absolute;left:45px;width:724px;background:var(--paper);box-shadow:0 4px 14px rgba(0,0,0,.18);overflow:hidden}
.sheet--outside{top:40px;height:560px}
.sheet--inside{top:630px;height:530px}
.panel{position:absolute;top:0;height:100%}
.photo{position:absolute}
.heading{font-family:"Oswald",Arial,sans-serif;font-weight:500;font-size:20px;letter-spacing:1px;color:var(--ink);display:flex;align-items:center;gap:8px}
.heading::after{content:"";flex:1;height:2px;background:var(--pink)}
.body-text{font-size:11px;line-height:1.55;color:var(--grey)}

/* outside left: services */
.services{left:0;width:241px;padding:22px 20px}
.services__intro{margin-top:14px;font-size:12.5px;line-height:1.35;color:var(--ink);font-weight:600}
.services__intro em{display:block;font-style:normal;color:var(--pink);font-size:17px;font-weight:600;line-height:1.25}
.services__list{list-style:none;margin-top:10px}
.services__list li{font-size:11px;color:var(--ink);line-height:1.75;display:flex;align-items:center;gap:6px}
.tick{width:10px;height:10px;flex:none}
.rent{position:absolute;left:0;bottom:0;width:241px;height:160px;background:var(--pink)}
.rent__text{position:absolute;left:20px;bottom:22px;color:#fff;font-family:"Oswald",Arial,sans-serif;font-size:17px;line-height:1.25;text-transform:uppercase}
.rent__text b{font-weight:500}

/* outside middle */
.back{left:241px;width:241px}
.back__city{left:0;top:0;width:241px;height:360px;background:linear-gradient(180deg,var(--sky) 0%,#c6cfd4 45%,var(--city) 100%)}
.back__band{position:absolute;left:0;bottom:0;width:241px;height:200px;background:var(--pink)}
.back__contact{position:absolute;left:60px;bottom:40px;color:#fff;font-size:9.5px;line-height:1.7}
.contact-row{display:flex;align-items:center;gap:5px}

/* outside right: cover */
.cover{left:482px;width:242px}
.brand{position:absolute;top:26px;left:0;width:242px;display:flex;align-items:center;justify-content:center;gap:7px}
.brand__dot{width:14px;height:14px;background:var(--pink)}
.brand__name{font-size:20px;font-weight:700;color:var(--ink);letter-spacing:-.3px}
.brand__tag{position:absolute;top:56px;width:242px;text-align:center;font-size:8.5px;color:var(--grey)}
.cover__city{left:0;top:82px;width:242px;height:360px;background:linear-gradient(180deg,#b9c7d3 0%,#8fa2b3 40%,#6a7d6f 100%)}
.cover__new{position:absolute;left:0;top:446px;width:242px;text-align:center;font-size:12px;color:var(--ink)}
.cover__new strong{color:var(--pink);font-weight:700}
.cover__call{position:absolute;left:0;top:468px;width:242px;text-align:center}
.cover__call span{display:inline-block;border:1.5px solid var(--pink);color:var(--pink);font-size:10px;font-weight:700;padding:2px 8px;letter-spacing:.5px}
.cover__phone{position:absolute;left:0;top:488px;width:242px;text-align:center;font-family:"Oswald",Arial,sans-serif;font-size:30px;line-height:1.2;color:var(--pink-dark)}
.web-bar{position:absolute;bottom:0;height:26px;background:var(--pink);color:#fff;font-size:11px;font-weight:700;display:flex;align-items:center;justify-content:center}

/* inside */
.about{left:0;width:241px;padding:22px 20px}
.about .body-text{margin-top:12px}
.about__resort{left:0;top:290px;width:241px;height:214px;background:linear-gradient(180deg,#b7d3e6 0%,#8fb06e 55%,#5aa3b8 100%)}
.inside__living{left:241px;top:0;width:483px;height:270px;background:linear-gradient(135deg,#d9d1c6 0%,#b9ab98 45%,#8c7f70 100%)}
.inside__kitchen{left:241px;top:276px;width:160px;height:125px;background:linear-gradient(160deg,#cfc7bb,#8a7f72)}
.inside__bedroom{left:241px;top:405px;width:160px;height:99px;background:linear-gradient(160deg,#e3ddd3,#a89c8c)}
.goal{left:420px;top:290px;width:285px;height:auto;padding:0}
.goal .body-text{margin-top:10px}
</style>
</head>
<body>

<section class="sheet sheet--outside">
  <div class="panel services">
    <h2 class="heading">OUR SERVICES</h2>
    <p class="services__intro">We provide many services for international patient who come to Marlowe medical center
      <em>for medical treatment , pleasure , business or visit</em>
      we also provide help with</p>
    <ul class="services__list">
      <li><svg class="tick" viewBox="0 0 10 10"><path d="M1 5l3 3 5-7" fill="none" stroke="var(--pink)" stroke-width="2"/></svg>Limousine service airport pick ups</li>
      <li><svg class="tick" viewBox="0 0 10 10"><path d="M1 5l3 3 5-7" fill="none" stroke="var(--pink)" stroke-width="2"/></svg>Cleaning services</li>
      <li><svg class="tick" viewBox="0 0 10 10"><path d="M1 5l3 3 5-7" fill="none" stroke="var(--pink)" stroke-width="2"/></svg>Concierge service</li>
      <li><svg class="tick" viewBox="0 0 10 10"><path d="M1 5l3 3 5-7" fill="none" stroke="var(--pink)" stroke-width="2"/></svg>Car rental services</li>
      <li><svg class="tick" viewBox="0 0 10 10"><path d="M1 5l3 3 5-7" fill="none" stroke="var(--pink)" stroke-width="2"/></svg>Prepaid services</li>
      <li><svg class="tick" viewBox="0 0 10 10"><path d="M1 5l3 3 5-7" fill="none" stroke="var(--pink)" stroke-width="2"/></svg>Immigration stay extend service</li>
    </ul>
  </div>
  <div class="rent" role="img" aria-label="Crimson rooftop silhouette band">
    <p class="rent__text"><b>We rent out</b><br>furnished apartment<br>for short term lease<br><b>30 days or more</b></p>
  </div>

  <div class="panel back">
    <div class="photo back__city" role="img" aria-label="Aerial photo of the downtown skyline with green parkland"></div>
    <div class="back__band" role="img" aria-label="Crimson rooftop silhouette band">
      <div class="back__contact">
        <div class="contact-row">2100 Harbor Point Blvd</div>
        <div class="contact-row">Suite 40, Marlowe, TX</div>
        <div class="contact-row"><svg width="8" height="8" viewBox="0 0 10 10"><path d="M2 1l2 2-1 1.5a6 6 0 0 0 2.5 2.5L7 6l2 2-1.5 1.5C5 9 1 5 .5 2z" fill="#fff"/></svg>555-014-2288</div>
        <div class="contact-row"><svg width="8" height="8" viewBox="0 0 10 10"><path d="M2 1l2 2-1 1.5a6 6 0 0 0 2.5 2.5L7 6l2 2-1.5 1.5C5 9 1 5 .5 2z" fill="#fff"/></svg>555-014-2289</div>
        <div class="contact-row">stay@harborlinestays.com</div>
      </div>
    </div>
  </div>

  <div class="panel cover">
    <div class="brand"><span class="brand__dot"></span><span class="brand__name">harborlinestays</span></div>
    <p class="brand__tag">Furnished homes for every stay</p>
    <div class="photo cover__city" role="img" aria-label="Photo of the city skyline at dusk"></div>
    <p class="cover__new">are you new in <strong>Houston Texas</strong></p>
    <div class="cover__call"><span>CALL FOR BOOKING</span></div>
    <p class="cover__phone">555-014-2288</p>
    <div class="web-bar" style="left:0;width:242px">www.harborlinestays.com</div>
  </div>
</section>

<section class="sheet sheet--inside">
  <div class="panel about">
    <h2 class="heading">ABOUT US</h2>
    <p class="body-text">We welcome guests from all over the world who come to the city for medical care, work or leisure. Our furnished apartments offer the comfort of home with the freedom of hotel service, so every guest can rest, recover and feel settled from day one. Our friendly team speaks many languages and is ready to help with every detail of your stay.</p>
  </div>
  <div class="photo about__resort" role="img" aria-label="Photo of a resort pool lined with palm trees"></div>
  <div class="photo inside__living" role="img" aria-label="Photo of a bright furnished living room with city views"></div>
  <div class="photo inside__kitchen" role="img" aria-label="Photo of a modern apartment kitchen"></div>
  <div class="photo inside__bedroom" role="img" aria-label="Photo of a furnished bedroom"></div>
  <div class="panel goal">
    <h2 class="heading">OUR GOAL</h2>
    <p class="body-text">Our goal is simple: make every guest feel at home, far from home. We plan each stay around your needs, from airport pick up to daily cleaning, so patients and families can focus on what matters most. Warm service, clean spaces and honest care guide everything we do.</p>
  </div>
  <div class="web-bar" style="left:0;width:241px">www.harborlinestays.com</div>
  <div class="web-bar" style="left:420px;width:304px">www.harborlinestays.com</div>
</section>

</body>
</html>
```